General Contractor ad set (3 ad campaign) directed at local realtors in Texas

We are a general contractor that performs remodels, restoration,and limited new construction. We need a set of facebook ads for our campaign. These three ads should be directed towards real estate owners, property managers, and brokers who have recently experienced property damage or need a "make ready to sell". The ad should implore them to use our service because of the value we are able to ad to properties and the efficiency at which we add that value. We would also like them to know that we are members of the GPBWG (prairie gulf beam workers guild)

website: www.drovamibuild.example
Updates

Target Market(s)

Real estate agents; Property Managers; House Flippers; Property owners

Industry/Entity Type

Construction Company

Colors
0455a3
f37122
f68d4d
f9ba93
cedeed
85abd2
3276b5

Requirements
Must have
• Clear and compelling depictiion of services.

```html
<!DOCTYPE html>
<html lang="en">
<head>
<meta charset="utf-8">
<title>Drovami – Ad Set</title>
<link rel="stylesheet" href="https://fonts.googleapis.com/css2?family=Alfa+Slab+One&family=Montserrat:wght@700&family=Oswald:wght@500&display=swap">
<style>
  :root{
    --navy:#2b3f8f;
    --blue:#0455a3;
    --blue-photo-a:#2f4fa3;
    --blue-photo-b:#263f8c;
    --orange:#f37122;
    --orange-photo-a:#f26a22;
    --orange-photo-b:#ea5f1c;
    --grey-photo-a:#f4f4f4;
    --grey-photo-b:#d6d6d6;
    --white:#ffffff;
    --stage:#dcdcdc;
  }
  *{box-sizing:border-box;margin:0;padding:0}
  html,body{width:1200px;height:800px;overflow:hidden;background:var(--stage)}
  .ad-set{position:relative;width:1200px;height:800px}
  .ad{position:absolute;top:203px;width:390px;height:390px;overflow:hidden}
  .ad--upgrade{left:6px}
  .ad--market{left:404px}
  .ad--storm{left:802px}
  .ad__photo{position:absolute;inset:0}
  .ad--upgrade .ad__photo{background:linear-gradient(135deg,var(--blue-photo-a),var(--blue-photo-b))}
  .ad--market .ad__photo{background:linear-gradient(160deg,var(--orange-photo-a),var(--orange-photo-b))}
  .ad--storm .ad__photo{background:linear-gradient(150deg,var(--grey-photo-a),var(--grey-photo-b))}

  .brand-badge{position:absolute;width:100px;height:100px;border-radius:50%;background:var(--white);
    display:flex;align-items:center;justify-content:center;
    font-family:"Montserrat",sans-serif;font-weight:700;font-size:17px;color:var(--navy)}
  .ad--upgrade .brand-badge{left:22px;top:30px}
  .ad--market .brand-badge{left:24px;top:21px}
  .brand-name{position:absolute;left:30px;top:78px;font-family:"Montserrat",sans-serif;font-weight:700;font-size:36px;color:var(--navy);letter-spacing:1px}

  .headline{position:absolute;left:16px;font-family:"Alfa Slab One",serif;color:var(--orange);text-transform:uppercase;line-height:1}
  .ad--upgrade .headline{top:165px;font-size:41px;line-height:1.02}
  .ad--market .headline{left:24px;top:145px;font-size:30px;color:var(--white)}
  .ad--storm .headline{left:22px;top:151px;font-size:30px}

  .subline{position:absolute;font-family:"Montserrat",sans-serif;font-weight:700;text-transform:uppercase}
  .ad--upgrade .subline{left:21px;top:249px;font-size:10px;color:var(--white);letter-spacing:.3px}
  .ad--market .subline,.ad--storm .subline{left:22px;top:213px;font-size:18px;color:var(--navy)}

  .phone{position:absolute;left:22px;top:282px;font-family:"Oswald",sans-serif;font-weight:500;font-size:23px;color:var(--orange)}
  .ad--market .phone{color:var(--white)}
  .url{position:absolute;left:22px;top:311px;font-family:"Montserrat",sans-serif;font-weight:700;font-size:9.5px;color:var(--white)}
  .ad--market .url,.ad--storm .url{color:var(--navy)}

  .partner-strip{position:absolute;left:20px;top:346px;width:189px;height:34px;background:var(--white);border-radius:2px;
    display:flex;align-items:center;gap:7px;padding:0 6px}
  .partner-strip .seal{width:24px;height:24px;border-radius:50%;background:#c9c9c9}
  .partner-strip .block{width:26px;height:18px;background:var(--blue)}
  .partner-strip .mark{width:22px;height:22px;background:#f3a6c8}
  .partner-strip .tag{width:60px;height:22px;background:#e1e1e1}
</style>
</head>
<body>
<main class="ad-set">

  <section class="ad ad--upgrade">
    <div class="ad__photo" role="img" aria-label="Blue-tinted photo of a house frame under construction with exposed roof trusses"></div>
    <div class="brand-badge">DROVAMI</div>
    <h2 class="headline">Time for an<br>upgrade?</h2>
    <p class="subline">Schedule your renovation project today!</p>
    <p class="phone">(855) 555 0142</p>
    <p class="url">WWW.DROVAMIBUILD.EXAMPLE</p>
    <div class="partner-strip" aria-label="Partner memberships">
      <span class="seal"></span><span class="block"></span><span class="mark"></span><span class="tag"></span>
    </div>
  </section>

  <section class="ad ad--market">
    <div class="ad__photo" role="img" aria-label="Orange-tinted photo of a suburban house with a for sale sign in the yard"></div>
    <div class="brand-badge">DROVAMI</div>
    <h2 class="headline">Is your house<br>market ready?</h2>
    <p class="subline">Call for an inspection</p>
    <p class="phone">(855) 555 0142</p>
    <p class="url">WWW.DROVAMIBUILD.EXAMPLE</p>
    <div class="partner-strip" aria-label="Partner memberships">
      <span class="seal"></span><span class="block"></span><span class="mark"></span><span class="tag"></span>
    </div>
  </section>

  <section class="ad ad--storm">
    <div class="ad__photo" role="img" aria-label="Faded grey photo of a house roof damaged by a fallen tree after a storm"></div>
    <div class="brand-name">DROVAMI</div>
    <h2 class="headline">Suffering from<br>storm damage?</h2>
    <p class="subline">Call for assistance</p>
    <p class="phone">(855) 555 0142</p>
    <p class="url">WWW.DROVAMIBUILD.EXAMPLE</p>
    <div class="partner-strip" aria-label="Partner memberships">
      <span class="seal"></span><span class="block"></span><span class="mark"></span><span class="tag"></span>
    </div>
  </section>

</main>
</body>
</html>
```